Verpackungsdesign für Zigarre
Zielgruppe
KALUN isteine Unternehmung im Baunebenbereich welche sich auf Kabelschächte und Schachtabdeckungen aus Chromstahl spezialisiert hat. Unsere Kunden sind Ingenieure, Planer, Netzbetreiber aus Telecom, Verkehr, Elektro und Industrie. Absatzpartner/Mittler sind auch grössere Bauunternehmungen. Die Ansprechpartner sind meist männlich zwischen 40 und 60 Jahre alt. Wir möchten unseren ausgewählten Kunden neben einer guten Flasche Rum welche wir schon separat gelabelt haben auch eine eigene Zigarre als Geschenk überreichen, da der Inhaber mit manchen Kunden die Leidenschaft Zigarren und Rum teilt. Dazu haben wir vorab1000 Zigarren in der Dominikanischen Republik nach den eigenen Vorgaben herstellen lassen welche, wir jetzt noch mit Banderole ausstatten möchten. Wir suchen ein schönes Design der Banderole (Bauchbinde) und auch eine kreative Verpackung für Gebinde von mehreren Zigarren (z.B. ein Einmachglas mit Etikette anstatt der Holzkistchen welche leider immer nach Gebrauch weggeschmissen werden)
Aufgabenstellung
Die Marke KALUN muss auf der Banderole als Sponsor (oder Überreicher) vermittelt werden. Für die Zigarre selbst haben wir den Namen vonerika ausgewählt. Da dies die erste eigene Zigarre wird soll der Beinamen Edition Eins verwendet werden. Evt. kann auch mit 2 Bauchbinden gearbeitet werden (KALUN und von erika und Edition Typ Eins separat... oder so...Wir benötigen ein Design und Format welches auch kurzfristig recht preisgünstig produziert werden kann. Erwartet wird ein Vorschlag bei welchem die Produktionsmöglichkeit abgeklärt wird (1000 - 5000 Stk. als Erstserie inkl. Druckofferte) Vielleicht bringt auch jemand einen ganz neuen kreativen schönen Vorschlag der Beschriftung...? Wir sind nicht auf Standardpapier eingeschossen - es muss einfach schön, kostengünstig und vorallem einprägsam sein. Bei Erfolg der Aktion überlegen wir uns noch weitere Formate und Zigarren herzustellen und vielleicht auch zu verkaufen anstatt zu verschen unter dem Namen von erika. Für die Verpackung von ganzen Gebinden (10-20 Stk. / Gebinde) suchen wir noch eine kreative Lösung welche sich von den klassischen Holzkistchen unterscheidet. Wir würden uns als Zusatz wünschen, dass der Designer auch dazu Vorschläge mit Beschriftung bringt. Die Farben von KALUN sind rot, chrom und schwarz... (siehe Website www.kalun-beispiel.com) von erika stelel ich mir in Gold vor. Evt. können die Firmenfarben von KALUN untergeordnet vertreten sein um dann komplett nur noch auf den Namen von erika später ohne KALUN mit Nachfolgeprodukten aufzusetzen um diese auch zu verkaufen.

```html
<!DOCTYPE html>
<html lang="de">
<head>
<meta charset="utf-8">
<title>von erika – Banderole Varianten</title>
<link rel="stylesheet" href="https://fonts.googleapis.com/css2?family=Arimo&family=Great+Vibes&family=Open+Sans:ital,wght@1,400&display=swap">
<style>
  :root {
    --paper: #ffffff;
    --ink: #111111;
    --band-dark: #1f1f1f;
    --band-mid: #2e2e2e;
    --oval-rim: #2b2b2b;
    --gold: #e3b23c;
    --gold-deep: #b8862a;
    --gold-light: #e9bd4e;
  }
  html, body {
    margin: 0;
    width: 1200px;
    height: 612px;
    overflow: hidden;
    background: var(--paper);
  }
  .sheet { display: block; width: 1200px; height: 612px; }
  .version-label {
    font-family: "Arimo", Arial, sans-serif;
    font-size: 26px;
    letter-spacing: 1px;
    fill: var(--ink);
  }
  .band-text {
    font-family: "Open Sans", Arial, sans-serif;
    font-style: italic;
    font-size: 17.5px;
    fill: var(--gold);
  }
  .band-text sup { font-size: 9px; }
  .cigar-name {
    font-family: "Great Vibes", cursive;
    font-size: 50px;
  }
  .cigar-name--gold { fill: var(--gold); }
  .cigar-name--dark { fill: var(--ink); }
  .gold-rule { stroke: var(--gold); stroke-width: 2; }
</style>
</head>
<body>
<svg class="sheet" viewBox="0 0 1200 612" xmlns="http://www.w3.org/2000/svg">
  <defs>
    <linearGradient id="bandShade" x1="0" y1="0" x2="1" y2="1">
      <stop offset="0" stop-color="var(--band-mid)"/>
      <stop offset="0.5" stop-color="var(--band-dark)"/>
      <stop offset="1" stop-color="var(--band-mid)"/>
    </linearGradient>
    <linearGradient id="goldFoil" x1="0" y1="0" x2="1" y2="1">
      <stop offset="0" stop-color="var(--gold-light)"/>
      <stop offset="1" stop-color="var(--gold-deep)"/>
    </linearGradient>
  </defs>

  <!-- Variante 4.1 -->
  <g class="variant variant--black">
    <text class="version-label" transform="translate(80 222) rotate(-90)">VERSION 4.1</text>
    <g class="band">
      <rect x="59" y="359" width="467" height="126" fill="url(#bandShade)"/>
      <line class="gold-rule" x1="59" y1="371" x2="526" y2="371"/>
      <line class="gold-rule" x1="59" y1="474" x2="526" y2="474"/>
      <text class="band-text" x="92" y="428">FROM KALUN®</text>
      <text class="band-text" x="376" y="428">EDITION EINS</text>
    </g>
    <g class="medallion">
      <ellipse cx="293" cy="421" rx="64" ry="103" fill="var(--oval-rim)"/>
      <ellipse cx="293" cy="421" rx="58" ry="95" fill="#111" stroke="var(--gold)" stroke-width="2"/>
      <g role="img" aria-label="Segelschiff-Illustration in Gold">
        <rect x="272" y="340" width="42" height="42" rx="6" fill="var(--gold)"/>
      </g>
      <text class="cigar-name cigar-name--gold" text-anchor="middle" transform="translate(296 440) rotate(-68)">von erika</text>
    </g>
  </g>

  <!-- Variante 4.2 -->
  <g class="variant variant--gold">
    <text class="version-label" transform="translate(714 222) rotate(-90)">VERSION 4.2</text>
    <g class="band">
      <rect x="693" y="359" width="467" height="126" fill="url(#bandShade)"/>
      <line class="gold-rule" x1="693" y1="371" x2="1160" y2="371"/>
      <line class="gold-rule" x1="693" y1="474" x2="1160" y2="474"/>
      <text class="band-text" x="726" y="428">FROM KALUN®</text>
      <text class="band-text" x="1010" y="428">EDITION EINS</text>
    </g>
    <g class="medallion">
      <ellipse cx="927" cy="421" rx="64" ry="103" fill="var(--oval-rim)"/>
      <ellipse cx="927" cy="421" rx="58" ry="95" fill="url(#goldFoil)" stroke="var(--gold)" stroke-width="2"/>
      <g role="img" aria-label="Segelschiff-Illustration in Schwarz">
        <rect x="906" y="340" width="42" height="42" rx="6" fill="#1a1a1a"/>
      </g>
      <text class="cigar-name cigar-name--dark" text-anchor="middle" transform="translate(930 440) rotate(-68)">von erika</text>
    </g>
  </g>
</svg>
</body>
</html>
```